Piano genealogy graphs template, for a large poster printing

Hello and thank you for your interest in my project.
I need a poster template, so I can create structures similar to the one I have uploaded. I want to completely replace or improve my poor previous design which is attached.
I need to be able to input names and dates into boxes of various colors, arrows pointing between boxes. I would also like to be able to label each graph (not each box).
I am looking at something that would be legible when printed, in a one consistent professional layout of 2A0 (around 1189x1682 mm) poster (I know it is large). The design template required here can include just few sample text boxes with sample flags on a suitable background, for me to multiply later and spread across the whole poster.
The positioning of the boxes is not important.
Please let me know if more clarification is required.
Thank you for your help.

Feel free to follow what I have attached in the file, or change the design completely.

UPDATE 4/12: I have uploaded two more graphs as an example. At this stage of the contest, I would like to have one of those graphs done, and I am planning to offer a 'freelance job' to one or two designers, who will be willing to do the whole 10 graphs on one poster.
Updates

Reason: Dear Designers, Since the project is rather complex and large-scale, I have decided to give everyone more time to work on their designs. I will consider extending it further if any of you require additional time. Best wishes, bronisław

Dear Designers, I would like to inform you that the contest for my poster is now closed and that I have assigned the prizes. I would like to thank all of you for submiting your high-quality designs, and for your participation. It was a great pleasure working with all of you. Due to the large size of the project itself (large number of graphs to be fitted on a single poster), I had to focus on providing feedback to only those designers who provided projects closest to what I was expecting at the early stages of the contest. I wish you all the best for the future, Kind regards, Bronisław

Target Market(s)

Pianists, historians

Industry/Entity Type

Printing

Requirements
Must have
• Consistent design, but allow to clearly delineate various genealogy trees.

```html
<!DOCTYPE html>
<html lang="en">
<head>
<meta charset="utf-8">
<title>Genealogical Trees of Pianists</title>
<link href="https://fonts.googleapis.com/css2?family=Catamaran:wght@700&family=Fira+Sans:wght@400;600&display=swap" rel="stylesheet">
<style>
  :root {
    --paper: #fefde6;
    --ink: #4a3c20;
    --card: #ffffff;
    --head-text: #fbf8ea;
    --flag-blue: #1a3fe0;
    --flag-white: #ffffff;
    --flag-red: #e8222c;
  }
  html, body { margin: 0; padding: 0; width: 960px; height: 1200px; overflow: hidden; background: var(--paper); }
  .poster { position: relative; width: 960px; height: 1200px; overflow: hidden; background: var(--paper); }
  .stage { position: absolute; left: 0; top: 0; width: 1200px; height: 1500px; transform: scale(0.8); transform-origin: 0 0; font-family: "Fira Sans", sans-serif; color: var(--ink); }
  .poster-title { position: absolute; left: 0; right: 0; top: 22px; margin: 0; text-align: center; font-family: "Catamaran", sans-serif; font-weight: 700; font-size: 45px; letter-spacing: 0.5px; color: var(--ink); }
  .connectors { position: absolute; left: 0; top: 0; width: 1200px; height: 1500px; }
  .connectors path { fill: none; stroke: var(--ink); stroke-width: 3; stroke-dasharray: 8 6; }

  .box { position: absolute; box-sizing: border-box; border: 3px solid var(--ink); border-radius: 18px; background: var(--card); overflow: hidden; }
  .box-head { position: relative; height: 54px; background: var(--ink); color: var(--head-text); font-weight: 600; font-size: 15px; line-height: 19px; text-align: center; display: flex; align-items: center; justify-content: center; padding-left: 34px; }
  .box-head .flag { position: absolute; left: 16px; top: 18px; }
  .box--single { background: var(--ink); }
  .box--single .box-head { height: 100%; }
  .student-list { list-style: none; margin: 0; padding: 18px 18px 0 10px; font-size: 13px; line-height: 17px; }
  .student-list li { display: flex; justify-content: space-between; align-items: center; padding-left: 0; margin-left: 0; }
  .student-list li .flag { margin: 1px 0; }
  .student-list li span { margin-left: 0; }
  .box--wide .student-list { padding-left: 18px; padding-right: 18px; }

  .flag { display: inline-flex; width: 24px; height: 15px; box-sizing: border-box; border: 1.5px solid var(--ink); flex: none; }
  .flag i { flex: 1; }
  .flag i:nth-child(1) { background: var(--flag-blue); }
  .flag i:nth-child(2) { background: var(--flag-white); }
  .flag i:nth-child(3) { background: var(--flag-red); }
</style>
</head>
<body>
<div class="poster">
<div class="stage">
  <h1 class="poster-title">Genealogical Trees of Pianists</h1>

  <svg class="connectors" viewBox="0 0 1200 1500" aria-hidden="true">
    <defs>
      <marker id="arrowhead" viewBox="0 0 10 10" refX="5" refY="5" markerWidth="4" markerHeight="4" orient="auto-start-reverse">
        <path d="M0 0 L10 5 L0 10 Z" style="fill:#4a3c20;stroke:none;stroke-dasharray:none"/>
      </marker>
    </defs>
    <path d="M583 1413 V1362" marker-end="url(#arrowhead)"/>
    <path d="M583 1280 V1244" marker-end="url(#arrowhead)"/>
    <path d="M583 1215 V1172" marker-end="url(#arrowhead)"/>
    <path d="M583 1215 H302 Q288 1215 288 1200 V1178" marker-end="url(#arrowhead)"/>
    <path d="M583 1215 H896 Q910 1215 910 1200 V1178" marker-end="url(#arrowhead)"/>
    <path d="M583 920 V864" marker-end="url(#arrowhead)"/>
    <path d="M429 1052 H276 Q262 1052 262 1038 V1010" marker-end="url(#arrowhead)"/>
    <path d="M771 1052 H925 Q939 1052 939 1038 V1010" marker-end="url(#arrowhead)"/>
    <path d="M429 832 H264 Q250 832 250 818 V800" marker-end="url(#arrowhead)"/>
    <path d="M771 749 H941 Q955 749 955 735 V708" marker-end="url(#arrowhead)"/>
    <path d="M583 611 V538" marker-end="url(#arrowhead)"/>
    <path d="M583 525 H209 Q195 525 195 511 V492" marker-end="url(#arrowhead)"/>
    <path d="M477 525 V420" marker-end="url(#arrowhead)"/>
    <path d="M583 525 H971 Q985 525 985 511 V492" marker-end="url(#arrowhead)"/>
    <path d="M715 525 V488" marker-end="url(#arrowhead)"/>
    <path d="M583 525 V332 Q583 318 597 318 H674 Q688 318 688 304 V284" marker-end="url(#arrowhead)"/>
    <path d="M490 343 V284" marker-end="url(#arrowhead)"/>
    <path d="M490 316 H209 Q195 316 195 302 V284" marker-end="url(#arrowhead)"/>
    <path d="M720 343 V330 Q720 318 734 318 H940 Q953 318 953 304 V284" marker-end="url(#arrowhead)"/>
    <path d="M1006 343 V284" marker-end="url(#arrowhead)"/>
  </svg>

  <!-- Row 1 -->
  <div class="box" style="left:72px;top:135px;width:244px;height:139px">
    <div class="box-head"><span class="flag"><i></i><i></i><i></i></span>Lucien Marvaud<br>(1916-2008) Students:</div>
    <ul class="student-list">
      <li><span>Jean-Marc Dellière (1947)</span><span class="flag"><i></i><i></i><i></i></span></li>
      <li><span>Jacques Vernoux (1947)</span><span class="flag"><i></i><i></i><i></i></span></li>
      <li><span>Jean-Luc Faucheret (1944)</span><span class="flag"><i></i><i></i><i></i></span></li>
    </ul>
  </div>
  <div class="box" style="left:343px;top:135px;width:244px;height:139px">
    <div class="box-head"><span class="flag"><i></i><i></i><i></i></span>Lucien Marvaud<br>(1916-2008) Students:</div>
    <ul class="student-list">
      <li><span>Jean-Marc Dellière (1947)</span><span class="flag"><i></i><i></i><i></i></span></li>
      <li><span>Jacques Vernoux (1947)</span><span class="flag"><i></i><i></i><i></i></span></li>
      <li><span>Jean-Luc Faucheret (1944)</span><span class="flag"><i></i><i></i><i></i></span></li>
    </ul>
  </div>
  <div class="box" style="left:613px;top:135px;width:244px;height:139px">
    <div class="box-head"><span class="flag"><i></i><i></i><i></i></span>Lucien Marvaud<br>(1916-2008) Students:</div>
    <ul class="student-list">
      <li><span>Jean-Marc Dellière (1947)</span><span class="flag"><i></i><i></i><i></i></span></li>
      <li><span>Jacques Vernoux (1947)</span><span class="flag"><i></i><i></i><i></i></span></li>
      <li><span>Jean-Luc Faucheret (1944)</span><span class="flag"><i></i><i></i><i></i></span></li>
    </ul>
  </div>
  <div class="box" style="left:884px;top:135px;width:244px;height:139px">
    <div class="box-head"><span class="flag"><i></i><i></i><i></i></span>Lucien Marvaud<br>(1916-2008) Students:</div>
    <ul class="student-list">
      <li><span>Jean-Marc Dellière (1947)</span><span class="flag"><i></i><i></i><i></i></span></li>
      <li><span>Jacques Vernoux (1947)</span><span class="flag"><i></i><i></i><i></i></span></li>
      <li><span>Jean-Luc Faucheret (1944)</span><span class="flag"><i></i><i></i><i></i></span></li>
    </ul>
  </div>

  <!-- Row 2 -->
  <div class="box box--wide" style="left:92px;top:343px;width:284px;height:139px">
    <div class="box-head"><span class="flag"><i></i><i></i><i></i></span>Lucien Marvaud<br>(1916-2008) Students:</div>
    <ul class="student-list">
      <li><span>Jean-Marc Dellière (1947)</span><span class="flag"><i></i><i></i><i></i></span></li>
      <li><span>Jacques Vernoux (1947)</span><span class="flag"><i></i><i></i><i></i></span></li>
      <li><span>Jean-Luc Faucheret (1944)</span><span class="flag"><i></i><i></i><i></i></span></li>
    </ul>
  </div>
  <div class="box box--single" style="left:397px;top:343px;width:173px;height:67px">
    <div class="box-head"><span class="flag"><i></i><i></i><i></i></span>Lucien Marvaud<br>(1916-2008)</div>
  </div>
  <div class="box" style="left:594px;top:343px;width:243px;height:139px">
    <div class="box-head"><span class="flag"><i></i><i></i><i></i></span>Lucien Marvaud<br>(1916-2008) Students:</div>
    <ul class="student-list">
      <li><span>Jean-Marc Dellière (1947)</span><span class="flag"><i></i><i></i><i></i></span></li>
      <li><span>Jacques Vernoux (1947)</span><span class="flag"><i></i><i></i><i></i></span></li>
      <li><span>Jean-Luc Faucheret (1944)</span><span class="flag"><i></i><i></i><i></i></span></li>
    </ul>
  </div>
  <div class="box" style="left:864px;top:343px;width:244px;height:139px">
    <div class="box-head"><span class="flag"><i></i><i></i><i></i></span>Lucien Marvaud<br>(1916-2008) Students:</div>
    <ul class="student-list">
      <li><span>Jean-Marc Dellière (1947)</span><span class="flag"><i></i><i></i><i></i></span></li>
      <li><span>Jacques Vernoux (1947)</span><span class="flag"><i></i><i></i><i></i></span></li>
      <li><span>Jean-Luc Faucheret (1944)</span><span class="flag"><i></i><i></i><i></i></span></li>
    </ul>
  </div>

  <!-- Row 3 -->
  <div class="box box--wide" style="left:112px;top:551px;width:289px;height:243px">
    <div class="box-head"><span class="flag"><i></i><i></i><i></i></span>Lucien Marvaud<br>(1916-2008) Students:</div>
    <ul class="student-list">
      <li><span>Jean-Marc Dellière (1947)</span><span class="flag"><i></i><i></i><i></i></span></li>
      <li><span>Jacques Vernoux (1947)</span><span class="flag"><i></i><i></i><i></i></span></li>
      <li><span>Jean-Luc Faucheret (1944)</span><span class="flag"><i></i><i></i><i></i></span></li>
      <li><span>Jean-Marc Dellière (1947)</span><span class="flag"><i></i><i></i><i></i></span></li>
      <li><span>Jacques Vernoux (1947)</span><span class="flag"><i></i><i></i><i></i></span></li>
      <li><span>Jean-Luc Faucheret (1944)</span><span class="flag"><i></i><i></i><i></i></span></li>
      <li><span>Jean-Marc Dellière (1947)</span><span class="flag"><i></i><i></i><i></i></span></li>
      <li><span>Jacques Vernoux (1947)</span><span class="flag"><i></i><i></i><i></i></span></li>
      <li><span>Jean-Luc Faucheret (1944)</span><span class="flag"><i></i><i></i><i></i></span></li>
    </ul>
  </div>
  <div class="box box--wide" style="left:429px;top:611px;width:342px;height:243px">
    <div class="box-head"><span class="flag"><i></i><i></i><i></i></span>Lucien Marvaud<br>(1916-2008) Students:</div>
    <ul class="student-list">
      <li><span>Jean-Marc Dellière (1947)</span><span class="flag"><i></i><i></i><i></i></span></li>
      <li><span>Jacques Vernoux (1947)</span><span class="flag"><i></i><i></i><i></i></span></li>
      <li><span>Jean-Luc Faucheret (1944)</span><span class="flag"><i></i><i></i><i></i></span></li>
      <li><span>Jean-Marc Dellière (1947)</span><span class="flag"><i></i><i></i><i></i></span></li>
      <li><span>Jacques Vernoux (1947)</span><span class="flag"><i></i><i></i><i></i></span></li>
      <li><span>Jean-Luc Faucheret (1944)</span><span class="flag"><i></i><i></i><i></i></span></li>
      <li><span>Jean-Marc Dellière (1947)</span><span class="flag"><i></i><i></i><i></i></span></li>
      <li><span>Jacques Vernoux (1947)</span><span class="flag"><i></i><i></i><i></i></span></li>
      <li><span>Jean-Luc Faucheret (1944)</span><span class="flag"><i></i><i></i><i></i></span></li>
    </ul>
  </div>
  <div class="box box--wide" style="left:804px;top:553px;width:283px;height:140px">
    <div class="box-head"><span class="flag"><i></i><i></i><i></i></span>Lucien Marvaud<br>(1916-2008) Students:</div>
    <ul class="student-list">
      <li><span>Jean-Marc Dellière (1947)</span><span class="flag"><i></i><i></i><i></i></span></li>
      <li><span>Jacques Vernoux (1947)</span><span class="flag"><i></i><i></i><i></i></span></li>
      <li><span>Jean-Luc Faucheret (1944)</span><span class="flag"><i></i><i></i><i></i></span></li>
    </ul>
  </div>

  <!-- Row 4 -->
  <div class="box" style="left:132px;top:860px;width:258px;height:140px">
    <div class="box-head"><span class="flag"><i></i><i></i><i></i></span>Lucien Marvaud<br>(1916-2008) Students:</div>
    <ul class="student-list">
      <li><span>Jean-Marc Dellière (1947)</span><span class="flag"><i></i><i></i><i></i></span></li>
      <li><span>Jacques Vernoux (1947)</span><span class="flag"><i></i><i></i><i></i></span></li>
      <li><span>Jean-Luc Faucheret (1944)</span><span class="flag"><i></i><i></i><i></i></span></li>
    </ul>
  </div>
  <div class="box box--wide" style="left:429px;top:920px;width:342px;height:243px">
    <div class="box-head"><span class="flag"><i></i><i></i><i></i></span>Lucien Marvaud<br>(1916-2008) Students:</div>
    <ul class="student-list">
      <li><span>Jean-Marc Dellière (1947)</span><span class="flag"><i></i><i></i><i></i></span></li>
      <li><span>Jacques Vernoux (1947)</span><span class="flag"><i></i><i></i><i></i></span></li>
      <li><span>Jean-Luc Faucheret (1944)</span><span class="flag"><i></i><i></i><i></i></span></li>
      <li><span>Jean-Marc Dellière (1947)</span><span class="flag"><i></i><i></i><i></i></span></li>
      <li><span>Jacques Vernoux (1947)</span><span class="flag"><i></i><i></i><i></i></span></li>
      <li><span>Jean-Luc Faucheret (1944)</span><span class="flag"><i></i><i></i><i></i></span></li>
      <li><span>Jean-Marc Dellière (1947)</span><span class="flag"><i></i><i></i><i></i></span></li>
      <li><span>Jacques Vernoux (1947)</span><span class="flag"><i></i><i></i><i></i></span></li>
      <li><span>Jean-Luc Faucheret (1944)</span><span class="flag"><i></i><i></i><i></i></span></li>
    </ul>
  </div>
  <div class="box" style="left:810px;top:860px;width:258px;height:140px">
    <div class="box-head"><span class="flag"><i></i><i></i><i></i></span>Lucien Marvaud<br>(1916-2008) Students:</div>
    <ul class="student-list">
      <li><span>Jean-Marc Dellière (1947)</span><span class="flag"><i></i><i></i><i></i></span></li>
      <li><span>Jacques Vernoux (1947)</span><span class="flag"><i></i><i></i><i></i></span></li>
      <li><span>Jean-Luc Faucheret (1944)</span><span class="flag"><i></i><i></i><i></i></span></li>
    </ul>
  </div>

  <!-- Rows 5–6 -->
  <div class="box box--single" style="left:178px;top:1100px;width:224px;height:67px">
    <div class="box-head"><span class="flag"><i></i><i></i><i></i></span>Lucien Marvaud<br>(1916-2008)</div>
  </div>
  <div class="box box--single" style="left:798px;top:1100px;width:224px;height:67px">
    <div class="box-head"><span class="flag"><i></i><i></i><i></i></span>Lucien Marvaud<br>(1916-2008)</div>
  </div>
  <div class="box box--single" style="left:471px;top:1279px;width:224px;height:67px">
    <div class="box-head"><span class="flag"><i></i><i></i><i></i></span>Lucien Marvaud<br>(1916-2008)</div>
  </div>
  <div class="box box--single" style="left:471px;top:1413px;width:224px;height:67px">
    <div class="box-head"><span class="flag"><i></i><i></i><i></i></span>Lucien Marvaud<br>(1916-2008)</div>
  </div>
</div>
</div>
</body>
</html>
```